Brindo like IOS/Android app for Okinawa Island - LumaTrail

LumaTrail is the name of the app
The closest thing that I can relate this app to is a region specific Brindo app. The app is for the island of Okinawa and is geared towards English speaking travelers. The style of app that I prefer is a look and feel similar to that of the new Nestora app, color should also be similar if not the same as the nestora app.

The app needs to have the following screens

LOGIN SCREEN
1. App login page with a login for chatterly button or create an account option. Personally I would like an image in the background with a real beachy feel, but don't do this if it messes with your design.

2. Depending on the choice of login there will need to be a second login screen to create the account. Nestora does this nicely.

PRIMARY HOME
primary page similar to the primary layout when you get into the nestora app.
This page is kind of like the home page of the app and should include the following items:
search field
upcoming events
popular things to do
featured restaurants
Featured Places to stay
area guides
Moving here
(this will allow the person to select, housing agencies, auto dealers, schools etc) These are essentially just quick searches.
Each selection should be listed so that the user can swipe to the left or right in order to view more listings under the categories listed above. It will not be the full list but rather a sample.

SIDEBAR POPOUT MENU
Popout sidebar that contains the following selections
Places to Eat
Things to do
Attractions
Beaches
Shop
Farmers Markets
Places to Stay
Schools & DayCare
Housing
Auto
Events
Account settings
Add a business

LIST VIEW
4. List view page for whatever category the user selected. This will show all the listings for the specific category: The top should also have the featured listings for that category

INDIVIDUAL LISTING
5. Listing page
This will include photos, description, hours, map(this can be a button to view the map or the map), Reviews with a leave a review option

AREA GUIDES
6. Area Guides. This is where the user will be able to select a specific area and learn about it. It should include an area where there can be a description, photos with a hero photo image, a map, popular local attractions or things to do, best restaurants in the area, places to stay etc.

PROFILE PAGE
7. Profile page for the user where they can make any updates they need to

Every page but the listing page should include the search bar. When the user clicks in it they should be able to see a drop down of quick select searches or run a regular search.

Logo
I have attached a logo that was made that needs a redesign. The map marker contains the logo for Okinawa within it so it does need to be similar.

If you have any questions or need clarification please send me a message. I will respond promptly.
Thank you,

```html
<!DOCTYPE html>
<html lang="en">
<head>
<meta charset="utf-8">
<title>LumaTrail – App Screens</title>
<link href="https://fonts.googleapis.com/css2?family=Source+Sans+3:wght@300;400;600;700&display=swap" rel="stylesheet">
<style>
:root{
  --bg:#c9c9c9;
  --pink:#e8606e;
  --pink-light:#f2838d;
  --pink-pale:#f6a4ab;
  --grey-dark:#5a5a5a;
  --grey-mid:#8a8a8a;
  --grey-line:#d9d9d9;
  --ink:#3f3f44;
  --white:#ffffff;
  --overlay:rgba(110,110,110,.78);
}
*{box-sizing:border-box;margin:0;padding:0}
html,body{width:1200px;height:789px;overflow:hidden}
body{background:radial-gradient(ellipse at 50% 40%,#e4e4e4 0%,var(--bg) 75%);font-family:"Source Sans 3",sans-serif;color:var(--ink)}
.screens{position:absolute;left:8px;top:195px;display:flex;gap:16px}
.screen{position:relative;width:224px;height:398px;background:var(--white);overflow:hidden;box-shadow:0 8px 24px rgba(0,0,0,.22)}

/* login */
.login{background:linear-gradient(160deg,var(--pink-light) 0%,var(--pink) 70%);color:var(--white)}
.login__link{position:absolute;right:12px;top:14px;font-size:10px;font-weight:300}
.brand{display:flex;align-items:center;gap:8px}
.login .brand{position:absolute;left:26px;top:122px}
.brand__dot{width:26px;height:26px;border-radius:50%;background:var(--white)}
.brand__name{font-size:26px;font-weight:600;letter-spacing:-.3px}
.login__actions{position:absolute;left:18px;right:18px;top:270px;text-align:center}
.btn{display:block;height:24px;line-height:24px;border-radius:12px;font-size:11px;font-weight:300}
.btn--solid{background:var(--white);color:var(--pink)}
.btn--ghost{border:1px solid var(--white);color:var(--white)}
.login__or{font-size:10px;margin:8px 0;font-weight:300}

/* home */
.icon-menu{position:absolute;left:12px;top:14px;width:16px}
.icon-menu span{display:block;height:2px;background:var(--pink);margin-bottom:3px}
.search-dot{position:absolute;width:22px;height:22px;border-radius:50%;background:var(--pink)}
.search-dot svg{position:absolute;left:5px;top:5px}
.home .search-dot{right:10px;top:38px}
.home__title{position:absolute;left:22px;top:48px;font-size:24px;font-weight:700;color:#55565b}
.carousel{position:absolute;left:0;width:224px;height:92px}
.carousel--1{top:104px}.carousel--2{top:210px}.carousel--3{top:316px}
.peek{position:absolute;top:0;height:84px;border-radius:4px}
.peek--left{left:-6px;width:40px}.peek--right{right:-10px;width:30px}
.peek.pink{background:var(--pink)}.peek.grey{background:#707070}
.chev{position:absolute;top:30px;width:10px;height:22px}
.chev--left{left:44px}.chev--right{right:44px}
.tile{position:absolute;left:68px;top:0;width:88px;height:86px;border-radius:4px;display:flex;align-items:center;justify-content:center;text-align:center}
.tile--events{background:linear-gradient(160deg,#d86a74,#b9434f)}
.tile--todo{background:linear-gradient(160deg,#7d8a6a,#4f5a45)}
.tile--food{background:linear-gradient(160deg,#e46756,#b53b36)}
.tile__label{color:var(--white);font-size:11px;font-weight:600;letter-spacing:1.6px;line-height:1.35;text-transform:uppercase}

/* splash */
.splash{display:flex;flex-direction:column;align-items:center;justify-content:center;gap:18px}
.splash__icon{width:110px;height:110px;border-radius:22px;background:linear-gradient(160deg,var(--pink-light),var(--pink))}
.splash__name{font-size:26px;font-weight:600;color:var(--ink)}

/* menu */
.menu__behind{position:absolute;inset:0;background:var(--overlay)}
.menu__behind .peek{width:30px;right:-6px;height:110px}
.menu__back{position:absolute;right:38px;top:20px}
.menu .search-dot{right:10px;top:20px}
.drawer{position:absolute;left:0;top:0;bottom:0;width:152px;background:var(--white);padding:14px 8px 0 6px}
.profile{display:flex;align-items:flex-end;justify-content:space-between;border-bottom:1px solid var(--pink-pale);padding-bottom:6px}
.avatar{width:20px;height:20px;border-radius:50%;background:var(--pink)}
.profile__text{text-align:right}
.profile__name{font-size:15px;font-weight:600;color:#55565b}
.profile__mail{font-size:6px;color:var(--grey-mid)}
.menu-list{list-style:none}
.menu-list li{display:flex;align-items:center;gap:9px;height:25.6px;border-bottom:1px solid var(--pink-pale);font-size:9.5px;color:var(--ink);font-weight:300}
.menu-list svg{width:12px;height:12px;flex:none}

/* restaurants */
.list__head{position:absolute;left:0;right:0;top:0;height:92px;background:var(--grey-dark)}
.list__head .icon-menu{left:6px;top:60px;width:10px}
.list__title{position:absolute;left:24px;top:54px;color:var(--white);font-size:11px;letter-spacing:1.6px;line-height:1.3;text-transform:uppercase}
.list .search-dot{right:12px;top:24px}
.entries{position:absolute;left:6px;right:10px;top:100px}
.entry{display:flex;gap:6px;padding:10px 0 8px;border-bottom:1px solid var(--pink-pale);height:96px}
.entry__media{width:54px;flex:none}
.entry__photo{width:54px;height:54px}
.photo--grill{background:linear-gradient(150deg,#7a4a23,#3a2414)}
.photo--thai{background:linear-gradient(150deg,#8a1c1c,#2d2b2a)}
.entry__rating{font-size:5px;color:var(--ink);margin-top:4px;white-space:nowrap}
.entry__rating b{color:#e9b437;font-weight:400}
.entry__name{font-size:10px;color:var(--ink);margin-bottom:4px}
.entry__meta{font-size:5.5px;color:var(--ink);line-height:1.5;font-weight:300}
</style>
</head>
<body>
<main class="screens">

  <section class="screen login" aria-label="Login screen">
    <span class="login__link">Login</span>
    <div class="brand"><span class="brand__dot"></span><span class="brand__name">LumaTrail</span></div>
    <div class="login__actions">
      <span class="btn btn--solid">Subscribe with Chatterly</span>
      <p class="login__or">or</p>
      <span class="btn btn--ghost">Create an Account</span>
    </div>
  </section>

  <section class="screen home" aria-label="Home screen">
    <div class="icon-menu"><span></span><span></span><span></span></div>
    <div class="search-dot"><svg width="12" height="12" viewBox="0 0 12 12"><circle cx="5" cy="5" r="3.3" fill="none" stroke="#fff" stroke-width="1.6"/><path d="M7.5 7.5L10.5 10.5" stroke="#fff" stroke-width="1.8"/></svg></div>
    <h1 class="home__title">Welcome.</h1>

    <div class="carousel carousel--1">
      <div class="peek peek--left pink"></div><div class="peek peek--right pink"></div>
      <svg class="chev chev--left" viewBox="0 0 10 22"><path d="M9 1L1 11l8 10" fill="none" stroke="#e8606e" stroke-width="1.2"/></svg>
      <div class="tile tile--events" role="img" aria-label="Concert crowd photo"><span class="tile__label">Upcoming<br>Events</span></div>
      <svg class="chev chev--right" viewBox="0 0 10 22"><path d="M1 1l8 10-8 10" fill="none" stroke="#e8606e" stroke-width="1.2"/></svg>
    </div>

    <div class="carousel carousel--2">
      <div class="peek peek--left grey"></div><div class="peek peek--right grey"></div>
      <svg class="chev chev--left" viewBox="0 0 10 22"><path d="M9 1L1 11l8 10" fill="none" stroke="#555" stroke-width="1.2"/></svg>
      <div class="tile tile--todo" role="img" aria-label="Outdoor festival photo"><span class="tile__label">Popular<br>Things<br>To Do</span></div>
      <svg class="chev chev--right" viewBox="0 0 10 22"><path d="M1 1l8 10-8 10" fill="none" stroke="#555" stroke-width="1.2"/></svg>
    </div>

    <div class="carousel carousel--3">
      <div class="peek peek--left pink"></div><div class="peek peek--right pink"></div>
      <svg class="chev chev--left" viewBox="0 0 10 22"><path d="M9 1L1 11l8 10" fill="none" stroke="#e8606e" stroke-width="1.2"/></svg>
      <div class="tile tile--food" role="img" aria-label="Grilled food photo"><span class="tile__label">Featured<br>Restaurant</span></div>
      <svg class="chev chev--right" viewBox="0 0 10 22"><path d="M1 1l8 10-8 10" fill="none" stroke="#e8606e" stroke-width="1.2"/></svg>
    </div>
  </section>

  <section class="screen splash" aria-label="Launch screen">
    <div class="splash__icon"></div>
    <span class="splash__name">LumaTrail</span>
  </section>

  <section class="screen menu" aria-label="Sidebar menu">
    <div class="menu__behind">
      <div class="peek pink" style="top:80px"></div>
      <div class="peek grey" style="top:210px;background:#555"></div>
      <div class="peek pink" style="top:320px"></div>
    </div>
    <svg class="menu__back" width="10" height="22" viewBox="0 0 10 22"><path d="M9 1L1 11l8 10" fill="none" stroke="#e8606e" stroke-width="1.2"/></svg>
    <div class="search-dot"><svg width="12" height="12" viewBox="0 0 12 12"><circle cx="5" cy="5" r="3.3" fill="none" stroke="#fff" stroke-width="1.6"/><path d="M7.5 7.5L10.5 10.5" stroke="#fff" stroke-width="1.8"/></svg></div>
    <nav class="drawer">
      <div class="profile">
        <span class="avatar"></span>
        <div class="profile__text"><div class="profile__name">NAME</div><div class="profile__mail">name.surname@mail.example</div></div>
      </div>
      <ul class="menu-list">
        <li><svg viewBox="0 0 12 12"><path d="M3 1v10M1.5 1v3h3V1M9 1c-1.5 1-1.5 4 0 5v5" fill="none" stroke="#333"/></svg>Places to Eat</li>
        <li><svg viewBox="0 0 12 12"><rect x="2" y="1.5" width="8" height="9.5" fill="none" stroke="#333"/><path d="M2 3.5h8" stroke="#333"/></svg>Things to do</li>
        <li><svg viewBox="0 0 12 12"><circle cx="6" cy="6" r="4" fill="none" stroke="#333"/><path d="M6 1v10M1 6h10M2.5 2.5l7 7M9.5 2.5l-7 7" stroke="#333" stroke-width=".6"/></svg>Attractions</li>
        <li><svg viewBox="0 0 12 12"><path d="M2 5c1-3 7-3 8 0zM6 5v6M3 11h6" fill="none" stroke="#333"/></svg>Beaches</li>
        <li><svg viewBox="0 0 12 12"><path d="M1 2h2l1.5 6h5.5l1-4.5H4" fill="none" stroke="#333"/><circle cx="5" cy="10" r="1" fill="#333"/><circle cx="9" cy="10" r="1" fill="#333"/></svg>Shop</li>
        <li><svg viewBox="0 0 12 12"><rect x="3" y="4" width="6" height="7" fill="none" stroke="#333"/><path d="M4 4V2h4v2" fill="none" stroke="#333"/></svg>Farmers Markets</li>
        <li><svg viewBox="0 0 12 12"><path d="M6 11S2.5 7 2.5 4.5a3.5 3.5 0 017 0C9.5 7 6 11 6 11z" fill="none" stroke="#333"/><circle cx="6" cy="4.5" r="1.2" fill="#333"/></svg>Places to Stay</li>
        <li><svg viewBox="0 0 12 12"><path d="M1 4l5-2.5L11 4 6 6.5z" fill="#333"/><path d="M3 5.5V8c1.5 1.3 4.5 1.3 6 0V5.5" fill="none" stroke="#333"/></svg>Schools &amp; DayCare</li>
        <li><svg viewBox="0 0 12 12"><path d="M1 3v7M1 8h10v2M1 6h10v2" fill="none" stroke="#333"/><rect x="2" y="5" width="3" height="2" fill="#333"/></svg>Housing</li>
        <li><svg viewBox="0 0 12 12"><path d="M2 6l1.5-3h5L10 6v3H2z" fill="none" stroke="#333"/><circle cx="4" cy="9.5" r="1" fill="#333"/><circle cx="8" cy="9.5" r="1" fill="#333"/></svg>Auto</li>
        <li><svg viewBox="0 0 12 12"><rect x="1.5" y="2" width="9" height="9" fill="none" stroke="#333"/><path d="M1.5 4.5h9M4 1v2M8 1v2" stroke="#333"/></svg>Events</li>
        <li><svg viewBox="0 0 12 12"><circle cx="6" cy="6" r="2.2" fill="none" stroke="#333" stroke-width="1.2"/><path d="M6 0.8v2M6 9.2v2M0.8 6h2M9.2 6h2M2.3 2.3l1.4 1.4M8.3 8.3l1.4 1.4M2.3 9.7l1.4-1.4M8.3 3.7l1.4-1.4" stroke="#333" stroke-width="1.2"/></svg>Account settings</li>
        <li><svg viewBox="0 0 12 12"><path d="M2 1h5l2.5 2.5V11H2z" fill="none" stroke="#333"/><path d="M7 1v3h2.5" fill="none" stroke="#333"/></svg>Add a business</li>
      </ul>
    </nav>
  </section>

  <section class="screen list" aria-label="Featured restaurant list">
    <header class="list__head">
      <div class="icon-menu"><span></span><span></span><span></span></div>
      <h2 class="list__title">Featured<br>Restaurant</h2>
      <div class="search-dot"><svg width="12" height="12" viewBox="0 0 12 12"><circle cx="5" cy="5" r="3.3" fill="none" stroke="#fff" stroke-width="1.6"/><path d="M7.5 7.5L10.5 10.5" stroke="#fff" stroke-width="1.8"/></svg></div>
    </header>
    <div class="entries">
      <article class="entry">
        <div class="entry__media"><div class="entry__photo photo--grill" role="img" aria-label="Grilled dish photo"></div><div class="entry__rating">25 Feedback · <b>★★★★★</b></div></div>
        <div><h3 class="entry__name">Harbor Lane Grill</h3><p class="entry__meta">Address: 4-7 Shore Road, Nago North, Okinawa Prefecture 900-0000<br>telephone: 000-555-0141<br>timetables: today open · 17–22</p></div>
      </article>
      <article class="entry">
        <div class="entry__media"><div class="entry__photo photo--thai" role="img" aria-label="Restaurant storefront at night photo"></div><div class="entry__rating">25 Feedback · <b>★★★★★</b></div></div>
        <div><h3 class="entry__name">Baan Lek Thai Kitchen</h3><p class="entry__meta">Address: 2-14 Palm Street, Central Ward, Okinawa Prefecture 900-0000<br>telephone: 000-555-0142<br>timetables: today open · 17–22</p></div>
      </article>
      <article class="entry">
        <div class="entry__media"><div class="entry__photo photo--grill" role="img" aria-label="Barbecue dish photo"></div><div class="entry__rating">25 Feedback · <b>★★★★</b>★</div></div>
        <div><h3 class="entry__name">Tidewater BBQ House</h3><p class="entry__meta">Address: 9-3 Coral Bay, Kin District, Okinawa Prefecture 900-0000<br>telephone: 000-555-0143<br>timetables: today open · 16–22</p></div>
      </article>
    </div>
  </section>

</main>
</body>
</html>
```